label bath salt on glass bottle

for our bath salts (Flavours Rose, Lavender, Lemongras, mountain herbs, Mint, Cashmere) we need a label in the size of 50mm height an 55mm wide.

Target Market(s)

Prestige stores

Font styles to use
Serif
Script

Colors

Designer to choose colors to be used in the design.

Requirements
Must have
• Name of the label:
• Headline: Badesalz (can be also written in two words) Bade Salz
• Describtion of the sel: Totes Meer (comes from Dead Sea)
• Name of the different fragrances:
• Rose
• Pfingstrose (Peony)
• Lemongras
• Alpenkräuter (mountain herbs)
• Minze (mint)
• Cashmere
• Lavendel (lavender)
Nice to have
• Made with love in Switzerland
• Logos:
• Use our LOGO in the attachment or just
• FENIVU
• Switzerland

```html
<!DOCTYPE html>
<html lang="de">
<head>
<meta charset="utf-8">
<title>FENIVU Bade Salz – Totes Meer – Rose</title>
<link rel="stylesheet" href="https://fonts.googleapis.com/css2?family=Tinos:ital,wght@0,400;0,700;1,400&family=Yellowtail&display=swap">
<style>
  :root {
    --canvas: #ffffff;
    --sea-mist: #f4f8f7;
    --sea-green: #68aa9b;
    --sea-teal: #5aa39a;
    --sea-sky: #3cb3ef;
    --sea-deep: #4d68b8;
    --sea-night: #4a59a3;
    --sand: #b08d6b;
    --sand-light: #c8a98a;
    --rose: #e5877e;
    --white: #ffffff;
  }
  html, body {
    margin: 0;
    padding: 0;
    width: 1200px;
    height: 2180px;
    overflow: hidden;
    background: var(--canvas);
  }
  .canvas {
    position: relative;
    width: 1200px;
    height: 2180px;
    background: var(--canvas);
  }
  .label {
    position: absolute;
    left: 0;
    top: 0;
    width: 1200px;
    height: 1090px;
    background: linear-gradient(
      to bottom,
      var(--sea-mist) 0%,
      var(--sea-green) 28%,
      var(--sea-teal) 52%,
      var(--sea-sky) 70%,
      var(--sea-deep) 88%,
      var(--sea-night) 100%
    );
    text-align: center;
    font-family: "Tinos", "Times New Roman", serif;
  }
  .brand {
    position: absolute;
    left: 0;
    right: 0;
    top: 148px;
    font-size: 56px;
    letter-spacing: 6px;
    color: var(--sand);
    line-height: 1;
  }
  .tagline {
    position: absolute;
    left: 0;
    right: 0;
    top: 290px;
    font-style: italic;
    font-size: 31px;
    letter-spacing: 2px;
    color: var(--sand);
    line-height: 1;
  }
  .headline {
    position: absolute;
    left: 0;
    right: 0;
    top: 405px;
    margin: 0;
    font-weight: 700;
    font-size: 128px;
    color: var(--white);
    line-height: 1;
  }
  .origin {
    position: absolute;
    left: 0;
    right: 0;
    top: 545px;
    font-size: 68px;
    color: var(--sand-light);
    line-height: 1;
  }
  .fragrance {
    position: absolute;
    left: 0;
    right: 0;
    top: 640px;
    font-family: "Yellowtail", cursive;
    font-size: 120px;
    color: var(--rose);
    line-height: 1;
    transform: rotate(-6deg);
  }
  .made-in {
    position: absolute;
    left: 0;
    right: 0;
    top: 978px;
    font-size: 25px;
    color: var(--sand-light);
    line-height: 1;
  }
</style>
</head>
<body>
  <main class="canvas">
    <section class="label" role="img" aria-label="Sea gradient label with a fine white wavy line pattern">
      <div class="brand">FENIVU</div>
      <div class="tagline">flavours of life</div>
      <h1 class="headline">Bade Salz</h1>
      <div class="origin">Totes Meer</div>
      <div class="fragrance">Rose</div>
      <div class="made-in">Made with love in Switzerland</div>
    </section>
  </main>
</body>
</html>
```